Modernize and improve usability of our webpage www.lerntausch-brolani.ch (4 languages, mostly static content)

Need to modernize and freshen up the webpages of our association: www.lerntausch-brolani.ch We offer apprenticeship exchanges within Switzerland and abroad. Young people can inform and enroll online. We do the matchmaking with work locations and organize logistics, stay overs etc.
The webpage needs to be in 4 languages (German, French, Italian and English). The main pages will be:
- Landing page: what we do, targeted to our apprentices / young people who enroll for the stages.
- Sup-Page: Registration form for interested apprentices to sign up for the program
- Sub-Page "Company", the firms who would like to send their apprentices on a internship and info on how to join the program
- Sub-Page "Host Family", private people who would be interested in hosting the apprentices (for free) during the stages. Find out about the reqiurements for the host families
- Sub-Page "About Us", who we are, executive team, board of director, our sponsor "Harmil Circle Switzerland"
- Footer: contact (E-Mail, Telephone, WhatsApp), Bank details (IBAN Number), Partnerlogo of Harmil-Circle (see uploaded jpg), Social-Media Links (Facebook, LinkedIn)

Target Market(s)

Young people looking for a "apprenticeship" stage within Switzerland or going from Switzerland abroad

Industry/Entity Type

Apprenticeships: cooks, builders, craftsman, office support, etc.

Number of Pages Required

5+ page

Font styles to use
Other font styles liked:
• Lato (sans serif)

Requirements
Must have
• use colors shown on uploaded PDF-Slides: Make the BLUE the MAIN color, the ORANGE as a secondary color
Nice to have
• Forms using e.g. google forms or survey-monkey forms (external links, no code). Matching & appealing visuals showing young apprentices (can use stock photos)

```html
<!DOCTYPE html>
<html lang="en">
<head>
<meta charset="utf-8">
<title>brolani – Apprenticeship Exchanges</title>
<link href="https://fonts.googleapis.com/css2?family=Lato:wght@300;400;700;900&display=swap" rel="stylesheet">
<style>
:root{
  --blue:#3d95f7;
  --blue-dark:#1f4f8e;
  --navy:#1d3b6f;
  --orange:#ff6a00;
  --orange-soft:#ff7a1a;
  --text:#3b4a63;
  --white:#fff;
}
*{margin:0;padding:0;box-sizing:border-box}
html,body{width:1200px;height:3909px;overflow:hidden}
body{position:relative;font-family:'Lato',sans-serif;color:var(--text);background:#fff}
.abs{position:absolute}
.btn{position:absolute;display:flex;align-items:center;justify-content:center;font-size:12px;font-weight:700;color:#fff;box-shadow:0 4px 10px rgba(0,0,0,.15)}
.btn-blue{background:var(--blue)}
.btn-orange{background:var(--orange)}
.btn-white{background:#fff;color:var(--blue)}
.label{position:absolute;font-size:13px;font-weight:700}
.ph{position:absolute}

/* header */
.site-header{position:absolute;left:0;top:0;width:1200px;height:75px;background:#fff}
.logo{position:absolute;left:126px;top:14px;font-size:34px;font-weight:900;color:var(--blue);letter-spacing:-.5px}
.nav a{position:absolute;top:30px;font-size:11px;color:var(--navy);text-decoration:none}
.nav a.active{color:var(--orange)}
.lang{position:absolute;left:993px;top:18px;width:82px;height:37px;background:#8fa2bf;color:#fff;font-size:11px;display:flex;align-items:center;padding-left:10px;gap:6px}
.lang i{display:block;width:20px;height:12px;background:#d9e1ef}

/* hero */
.hero{position:absolute;left:0;top:75px;width:1200px;height:470px;background:linear-gradient(135deg,#24508f,#2f6bbd 55%,#1f4a85)}
.hero h1{position:absolute;left:0;top:135px;width:1200px;text-align:center;color:#fff;font-size:38px;font-weight:300;line-height:46px}
.hero h1 b{font-weight:900}

/* what we do */
.wwd-head{position:absolute;left:125px;top:738px;width:340px;font-size:23px;line-height:30px;color:var(--navy)}
.job{position:absolute;width:182px;height:199px;display:flex;align-items:flex-end;justify-content:center;padding-bottom:30px;color:#fff;font-weight:700;font-size:14px}
.job.blue{background:linear-gradient(180deg,#9bb6d4,#3d85d9)}
.job.orange{background:linear-gradient(180deg,#c9a67f,#ff7a1a)}

/* companies */
.companies{position:absolute;left:0;top:1112px;width:1200px;height:625px;background:var(--blue)}
.sec-title{position:absolute;left:0;width:1200px;text-align:center;font-size:23px;line-height:27px;color:#fff}
.co-img{position:absolute;width:300px;height:187px}
.co-name{position:absolute;width:300px;text-align:center;color:#fff;font-weight:700;font-size:15px}
.co-text{position:absolute;width:260px;text-align:center;color:#fff;font-size:10.5px;line-height:19px}

/* host family */
.host{position:absolute;left:0;top:1737px;width:1200px;height:548px;background:var(--orange)}

/* about */
.about-head{position:absolute;left:0;top:2400px;width:1200px;text-align:center;font-size:23px;line-height:30px;color:var(--navy)}
.about-text{position:absolute;left:240px;top:2505px;width:720px;text-align:center;font-size:10.5px;line-height:19px;color:var(--navy)}
.team-card{position:absolute;width:250px;height:162px;background:var(--orange)}
.team-card .dots{position:absolute;right:8px;bottom:8px;width:48px;height:66px;background-image:radial-gradient(circle,rgba(255,255,255,.5) 1.2px,transparent 1.5px);background-size:12px 12px}
.team-photo{position:absolute;width:138px;height:138px;border-radius:50% 50% 50% 0;background:linear-gradient(180deg,#d7dce4,#8d97a6)}
.team-name{position:absolute;color:#fff;font-size:15px;font-weight:700}
.team-role{position:absolute;color:#fff;font-size:11px}

/* apply */
.apply{position:absolute;left:0;top:3061px;width:1200px;height:410px;background:var(--blue);overflow:hidden}
.survey-opt{position:absolute;left:742px;font-size:11px;color:#fff;display:flex;align-items:center;gap:10px}
.survey-opt i{display:block;width:11px;height:11px;border:1.5px solid #fff;border-radius:50%}
.survey-opt i.on{background:radial-gradient(circle,#fff 2.5px,transparent 3px)}

/* footer */
.footer{position:absolute;left:0;top:3471px;width:1200px;height:438px;background:var(--blue-dark);color:#fff}
.f-title{position:absolute;font-size:14px;font-weight:700;color:#fff}
.f-link{position:absolute;font-size:10px;color:#fff}
.f-item{position:absolute;font-size:12px;color:#fff;display:flex;gap:10px;align-items:flex-start}
.f-item svg{flex:none;margin-top:1px}
.social{position:absolute;top:311px;width:30px;height:30px;border-radius:50%}
</style>
</head>
<body>

<header class="site-header">
  <div class="logo">brolani</div>
  <nav class="nav">
    <a class="active" style="left:424px">Home</a>
    <a style="left:480px">Company</a>
    <a style="left:552px">Host Family</a>
    <a style="left:638px">About Us</a>
    <a style="left:710px">Contact Us</a>
    <a style="left:825px;color:var(--orange);font-weight:700">&#9679; Login</a>
  </nav>
  <div class="btn btn-blue" style="left:880px;top:18px;width:100px;height:37px;box-shadow:none">Apply Now!</div>
  <div class="lang"><i></i>En <span style="margin-left:14px;font-size:8px">&#9660;</span></div>
</header>

<section class="hero" role="img" aria-label="Photo of a young cook plating food in a professional kitchen, blue tinted">
  <h1>We offer <b>apprenticeship</b> exchanges within<br><b>Switzerland and abroad</b></h1>
  <div class="btn btn-orange" style="left:536px;top:249px;width:125px;height:36px">Contact Us Today</div>
</section>

<section class="what-we-do">
  <div class="label" style="left:125px;top:705px;color:#e0432b">What We Do</div>
  <h2 class="wwd-head" style="font-weight:400">Harmil Circle Switzerland/Liechtenstein mainly supports this program with the objective of promoting the mobility of apprentices</h2>
  <div class="btn btn-blue" style="left:125px;top:903px;width:113px;height:37px">Apply now!</div>
  <div class="job blue" style="left:481px;top:732px" role="img" aria-label="Photo of a cook cutting vegetables">Cooks</div>
  <div class="job orange" style="left:687px;top:619px" role="img" aria-label="Photo of a builder in a hard hat">Builders</div>
  <div class="job blue" style="left:687px;top:843px" role="img" aria-label="Photo of a craftsman working wood">Craftsman</div>
  <div class="job blue" style="left:894px;top:732px" role="img" aria-label="Photo of an office support worker with headset">Office Support</div>
</section>

<section class="companies">
  <div class="label" style="left:0;width:1200px;text-align:center;top:84px;color:#fff">Companies</div>
  <h2 class="sec-title" style="top:118px;font-weight:400">Every successful company builds on well educated and<br>motivated professionals.</h2>

  <div class="co-img" style="left:125px;top:199px;background:linear-gradient(180deg,#3b2a2a,#b04a2a)" role="img" aria-label="Photo of a lit arena building at night"></div>
  <div class="co-img" style="left:450px;top:199px;background:linear-gradient(180deg,#4a4a4a,#e08a2a)" role="img" aria-label="Photo of a chef cooking with flames"></div>
  <div class="co-img" style="left:775px;top:199px;background:linear-gradient(180deg,#d9d2c4,#3aa08a)" role="img" aria-label="Photo of hands measuring fabric"></div>
  <div class="abs" style="left:150px;top:360px;width:250px;height:30px;background:var(--blue)"></div>
  <div class="abs" style="left:475px;top:360px;width:250px;height:30px;background:var(--blue)"></div>
  <div class="abs" style="left:800px;top:360px;width:250px;height:30px;background:var(--blue)"></div>

  <div class="co-name" style="left:125px;top:383px">Felsberg Architektur AG</div>
  <div class="co-name" style="left:450px;top:383px">Marend AG</div>
  <div class="co-name" style="left:775px;top:383px">Tessura</div>
  <p class="co-text" style="left:145px;top:410px">Our office Felsberg Architektur AG, with headquarters in Seewil near Zurich, is primarily active in the planning and...</p>
  <p class="co-text" style="left:470px;top:410px">Die Firma Marend AG is a world-renowned manufacturer of Druckreaktorsystemen and Glasanlagen as Reaktoren, Filter ...</p>
  <p class="co-text" style="left:795px;top:410px">tessura, the Swiss technical school for fashion and design, has a leading position in the Swiss fashion landscape.</p>

  <div class="btn btn-orange" style="left:525px;top:514px;width:150px;height:38px">View All Companies</div>
</section>

<section class="host">
  <div class="label" style="left:200px;top:128px;color:#fff">Host Family</div>
  <h2 class="abs" style="left:200px;top:165px;width:340px;font-size:23px;line-height:30px;font-weight:400;color:#fff">Lorem Ipsum is simply dummy text of the printing and typesetting industry.</h2>
  <p class="abs" style="left:200px;top:275px;width:350px;font-size:10.5px;line-height:19px;color:#fff">It is a long established fact that a reader will be distracted by the readable content of a page when looking at its layout. The point of using Lorem Ipsum is that it has a more-or-less normal distribution of letters, as opposed to using 'Content here, content here...</p>
  <div class="btn btn-blue" style="left:200px;top:376px;width:151px;height:36px">About The Host Families</div>
  <div class="ph" style="left:612px;top:83px;width:388px;height:387px;border-radius:50% 50% 50% 0;background:linear-gradient(160deg,#c9b59a,#e8e2d8 45%,#8a6a4a)" role="img" aria-label="Photo of young apprentices cooking with a chef in a kitchen"></div>
</section>

<section class="about">
  <div class="label" style="left:0;width:1200px;text-align:center;top:2356px;color:var(--blue)">About Us</div>
  <h2 class="about-head" style="font-weight:400">Brolani has been organizing the exchange of apprentices between<br>different cultural and language regions within Switzerland as well as<br>with other countries for more than 19 years.</h2>
  <p class="about-text">Primary participants are all apprentices who are completing their basic vocational education and training.<br>Once registered for the exchange, brolani will find a suitable exchange company and an appropriate accommodation, where the apprentice will go through an exchange of at least three weeks. Harmil Circle Switzerland/Liechtenstein mainly supports this program with the objective of promoting the mobility of apprentices.</p>
  <div class="btn btn-blue" style="left:524px;top:2606px;width:150px;height:35px">Discover More About</div>

  <div class="team-card" style="left:200px;top:2678px"><div class="dots"></div></div>
  <div class="team-photo" style="left:224px;top:2618px" role="img" aria-label="Portrait of a co-managing director"></div>
  <div class="team-name" style="left:224px;top:2774px">Lena Amsler</div>
  <div class="team-role" style="left:224px;top:2793px">Co-Managing Director</div>

  <div class="team-card" style="left:475px;top:2754px"><div class="dots"></div></div>
  <div class="team-photo" style="left:499px;top:2692px" role="img" aria-label="Portrait of a co-managing director"></div>
  <div class="team-name" style="left:499px;top:2849px">Sara Keller</div>
  <div class="team-role" style="left:499px;top:2868px">Co-Managing Director</div>

  <div class="team-card" style="left:750px;top:2678px"><div class="dots"></div></div>
  <div class="team-photo" style="left:774px;top:2617px" role="img" aria-label="Portrait of the contact person for Romandie"></div>
  <div class="team-name" style="left:774px;top:2774px">Giulia Moretti</div>
  <div class="team-role" style="left:774px;top:2793px">Contact for Romandie</div>

  <div class="btn btn-blue" style="left:544px;top:2946px;width:112px;height:37px">View All Team</div>
</section>

<div class="abs" style="left:643px;top:3011px;width:430px;height:430px;border-radius:50%;background:var(--orange-soft)"></div>
<section class="apply">
  <div class="abs" style="left:643px;top:-50px;width:430px;height:430px;border-radius:50%;background:linear-gradient(180deg,var(--orange-soft) 20%,rgba(61,149,247,1) 100%)"></div>
  <div class="label" style="left:125px;top:88px;color:#fff">Apply now!</div>
  <h2 class="abs" style="left:125px;top:120px;width:480px;font-size:31px;line-height:36px;font-weight:300;color:#fff"><b style="font-weight:900">Brolani organizes the exchange of apprentices</b> from different language and cultural areas in <b style="font-weight:900">Switzerland and abroad.</b></h2>
  <div class="btn btn-white" style="left:125px;top:289px;width:113px;height:36px">Apply now!</div>

  <div class="abs" style="left:700px;top:5px;width:316px;text-align:center;font-size:21px;line-height:27px;font-weight:300;color:#fff">Employee engagement<br><span style="font-weight:700;text-decoration:underline">Survey</span></div>
  <div class="abs" style="left:742px;top:72px;font-size:12px;font-weight:700;color:#fff">I am inspired to meet my goals at work.</div>
  <div class="survey-opt" style="top:108px"><i></i>Strongly agree</div>
  <div class="survey-opt" style="top:131px"><i class="on"></i>Agree</div>
  <div class="survey-opt" style="top:154px"><i></i>Neither agree not disagree</div>
  <div class="survey-opt" style="top:177px"><i></i>Disagree</div>
  <div class="survey-opt" style="top:200px"><i></i>Strongly disagree</div>
  <div class="btn btn-orange" style="left:742px;top:239px;width:112px;height:35px">Next</div>

  <div class="ph" style="left:950px;top:54px;width:240px;height:356px;border-radius:120px 120px 0 0;background:linear-gradient(180deg,#e9e6e2,#ffffff 60%,#cfd6df)" role="img" aria-label="Photo of a smiling young man in shirt and tie pointing at the survey"></div>
</section>

<footer class="footer">
  <div class="abs" style="left:125px;top:105px;font-size:64px;font-weight:900;line-height:70px;color:#fff">brolani</div>
  <p class="abs" style="left:125px;top:203px;width:215px;font-size:10px;line-height:14px">Brolani organizes the exchange of apprentices from different language and cultural areas in Switzerland and abroad.</p>

  <div class="f-title" style="left:406px;top:107px">Contact Us</div>
  <div class="f-item" style="left:406px;top:144px"><svg width="12" height="12" viewBox="0 0 24 24"><path fill="#ff6a00" d="M6.6 10.8a15 15 0 006.6 6.6l2.2-2.2a1 1 0 011-.25 11.4 11.4 0 003.6.57 1 1 0 011 1V20a1 1 0 01-1 1A17 17 0 013 4a1 1 0 011-1h3.5a1 1 0 011 1c0 1.25.2 2.45.57 3.6a1 1 0 01-.25 1z"/></svg>+41 (0) 33 000 12 34</div>
  <div class="f-item" style="left:406px;top:174px"><svg width="12" height="12" viewBox="0 0 24 24"><circle cx="12" cy="12" r="9" fill="none" stroke="#ff6a00" stroke-width="2.5"/></svg>+41 79 000 45 67</div>
  <div class="f-item" style="left:406px;top:205px;font-size:11px"><svg width="12" height="12" viewBox="0 0 24 24"><rect x="3" y="5" width="18" height="14" fill="#ff6a00"/><path d="M3 6l9 7 9-7" stroke="#1f4f8e" stroke-width="2" fill="none"/></svg>info@brolani.ch</div>
  <div class="f-item" style="left:406px;top:236px;font-size:11px;line-height:15px"><svg width="12" height="12" viewBox="0 0 24 24"><path fill="#ff6a00" d="M12 2a7 7 0 00-7 7c0 5 7 13 7 13s7-8 7-13a7 7 0 00-7-7zm0 9.5A2.5 2.5 0 1112 6a2.5 2.5 0 010 5.5z"/></svg><span>Brolani<br>Lindenweg 4, 8600 Musterdorf</span></div>

  <div class="f-title" style="left:650px;top:107px">Quick Links</div>
  <div class="f-link" style="left:650px;top:142px">Home</div>
  <div class="f-link" style="left:650px;top:164px">Company</div>
  <div class="f-link" style="left:650px;top:187px">Host Family</div>
  <div class="f-link" style="left:650px;top:209px">About Us</div>
  <div class="f-link" style="left:650px;top:232px">Contact Us</div>

  <div class="f-title" style="left:818px;top:107px">Subscribe Newsletter</div>
  <div class="abs" style="left:818px;top:151px;width:275px;height:37px;background:#fff;color:var(--navy);font-size:10px;padding:12px 18px">name@email.com</div>
  <div class="btn btn-blue" style="left:818px;top:204px;width:87px;height:35px;box-shadow:none">Submit</div>

  <div class="f-link" style="left:125px;top:321px">© 2023 <span style="color:var(--blue)">Brolani</span>. All Rights Reserved.</div>
  <div class="f-link" style="left:405px;top:321px">Imprint &nbsp;&nbsp; I &nbsp;&nbsp; Privacy policy</div>
  <div class="social" style="left:650px;background:var(--blue)" role="img" aria-label="Social network link"></div>
  <div class="social" style="left:688px;background:var(--orange)" role="img" aria-label="Professional network link"></div>
  <div class="abs" style="left:818px;top:312px;font-size:25px;font-weight:700;color:#fff;display:flex;align-items:center;gap:10px">Harmil Circle<span style="display:block;width:28px;height:28px;border-radius:50%;background:#f0b323"></span></div>
  <svg class="abs" style="left:1128px;top:312px" width="20" height="24" viewBox="0 0 20 24"><path d="M10 0L20 24 10 18 0 24z" fill="var(--blue)"/></svg>
</footer>

</body>
</html>
```